Business Card Design

I am a Building Surveyor and run my own Building Consultat company, providing professional advice and services to builders, architects, designers, owners, etc.

Industry/Entity Type

Business

Contact Information for Business Card

Dorwen Fasque BBldgSurv (Hons)
Managing Director

47 Marlow Crest, Kelvoth Downs WA 6158
Mobile 0498 153 607
Email Dorwen.fasque@ridgeplumbav.com

Requirements
Must have
• I would like the back of the business card to be one colour (a shade of either black or maroon, matching the colours of my logo). Positioned in the centre on the back of the business card is to be my logo.

The front of the card is to be white, with my contact information in either black or maroon. The ADBldgSurv after my name should be in a smaller font size than my name. I would also like a small logo somewhere on this side of the card.

```html
<!DOCTYPE html>
<html lang="en">
<head>
<meta charset="utf-8">
<title>Marlow Building Consultants – Business Card</title>
<link href="https://fonts.googleapis.com/css2?family=Josefin+Sans:wght@300;400&display=swap" rel="stylesheet">
<style>
  :root {
    --backdrop: #2a2a2a;
    --card-grey: #4a4a48;
    --card-white: #ffffff;
    --maroon: #7a1f24;
    --ink-light: #f2f2f0;
    --rule: #bdbdb8;
  }
  * { box-sizing: border-box; margin: 0; padding: 0; }
  html, body {
    width: 1200px; height: 900px; overflow: hidden;
    background: var(--backdrop);
    font-family: "Josefin Sans", "Helvetica Neue", sans-serif;
    font-weight: 300;
  }
  .stage {
    position: relative; width: 1200px; height: 900px;
    display: flex; align-items: center; justify-content: center; gap: 60px;
  }
  .card {
    width: 490px; height: 300px; position: relative; overflow: hidden;
    box-shadow: 0 18px 40px rgba(0,0,0,.55);
  }
  /* front */
  .card-front { display: flex; background: var(--card-grey); }
  .front-brand {
    width: 186px; background: var(--card-white);
    display: flex; align-items: center; justify-content: center; gap: 8px;
    padding: 0 10px;
  }
  .brand-dot {
    width: 16px; height: 16px; border-radius: 50%;
    border: 2px solid var(--maroon); flex: none;
  }
  .brand-name-small {
    color: var(--maroon); font-size: 10.5px; font-weight: 400;
    letter-spacing: .08em; text-transform: uppercase; line-height: 1.35;
  }
  .front-details {
    flex: 1; color: var(--ink-light); padding: 44px 22px 0 26px;
  }
  .person-name { font-size: 19px; letter-spacing: .1em; text-transform: uppercase; }
  .person-title { font-size: 10px; margin-top: 4px; letter-spacing: .03em; }
  .address { font-size: 11px; margin-top: 22px; line-height: 1.6; }
  .contact { font-size: 11px; margin-top: 18px; line-height: 1.75; }
  /* back */
  .card-back {
    background: var(--card-grey);
    display: flex; align-items: center; justify-content: center;
  }
  .back-brand { display: flex; align-items: center; gap: 16px; }
  .brand-ring {
    width: 62px; height: 62px; border-radius: 50%;
    border: 3px solid var(--ink-light); flex: none;
  }
  .brand-name-large {
    color: var(--ink-light); font-weight: 400; text-transform: uppercase;
    letter-spacing: .1em; line-height: 1.15;
    border-bottom: 1px solid var(--rule); padding-bottom: 6px;
  }
  .brand-name-large .word-main { display: block; font-size: 34px; }
  .brand-name-large .word-sub { display: block; font-size: 12px; letter-spacing: .16em; text-align: center; }
</style>
</head>
<body>
  <main class="stage">
    <section class="card card-front" aria-label="Business card front">
      <div class="front-brand">
        <span class="brand-dot"></span>
        <span class="brand-name-small">Marlow<br>Building Consultants</span>
      </div>
      <div class="front-details">
        <p class="person-name">Dorwen Fasque</p>
        <p class="person-title">ADBldgSurv Director</p>
        <p class="address">47 Marlow Crest,<br>Kelvoth Downs WA 6158</p>
        <p class="contact">phone: 0498 153 607<br>email: Dorwen.fasque@ridgeplumbav.com</p>
      </div>
    </section>
    <section class="card card-back" aria-label="Business card back">
      <div class="back-brand">
        <span class="brand-ring"></span>
        <p class="brand-name-large">
          <span class="word-main">Marlow</span>
          <span class="word-sub">Building Consultants</span>
        </p>
      </div>
    </section>
  </main>
</body>
</html>
```